Business Card Design - Carrington Hill Lodge

We are looking at a new design for our business cards that has a modern and professional look. We run a residential aged care facility focussing on the care of residents. The cards will be used for potential clients, consultants and business opportunities in this sector. Blue and white is our main colours and would to see these colours incorporated in the design.
Industry/Entity Type
Business
Contact Information for Business Card
Carrington Hill Lodge, Darren Pelham, dpelham@carringtonhilllodge.com.au, Finance Manager, 0491 736 208, BCom, 48 Yarrabee Way, Birchwood, Qld 4215.

```html
<!DOCTYPE html>
<html lang="en">
<head>
<meta charset="utf-8">
<title>Carrington Hill Lodge – Business Card</title>
<link rel="stylesheet" href="https://fonts.googleapis.com/css2?family=Source+Sans+3:ital,wght@0,400;0,600;1,400&display=swap">
<style>
  :root {
    --page: #9a9c9b;
    --card-white: #f1f1f3;
    --brand-blue: #3f6c8c;
    --warm-grey: #918884;
    --text-dark: #3b3b3d;
    --text-muted: #8a8483;
    --rule: #c9c9cc;
    --back-light: #ecebee;
  }
  * { box-sizing: border-box; margin: 0; padding: 0; }
  html, body { width: 1105px; height: 1200px; overflow: hidden; }
  body {
    background: var(--page);
    font-family: "Source Sans 3", "Myriad Pro", Arial, sans-serif;
    position: relative;
  }
  .card {
    position: absolute;
    left: 180px;
    width: 745px;
    height: 428px;
    overflow: hidden;
  }
  .card--front { top: 110px; background: var(--card-white); }
  .card--back { top: 635px; background: var(--warm-grey); }

  /* Front: brand block */
  .brand {
    position: absolute;
    left: 30px;
    top: 110px;
    width: 300px;
    text-align: center;
  }
  .brand__dot {
    width: 100px; height: 100px;
    border-radius: 50%;
    background: var(--brand-blue);
    margin: 0 auto 18px;
  }
  .brand__name {
    color: var(--brand-blue);
    font-weight: 600;
    font-size: 22px;
    letter-spacing: 1px;
    text-transform: uppercase;
    line-height: 1.1;
    white-space: nowrap;
  }

  .divider {
    position: absolute;
    left: 352px; top: 92px;
    width: 1px; height: 220px;
    background: var(--rule);
  }

  /* Front: contact details */
  .contact {
    position: absolute;
    left: 384px; top: 90px;
    color: var(--text-dark);
  }
  .contact__name {
    color: var(--brand-blue);
    font-weight: 600;
    font-size: 27px;
    line-height: 1.1;
  }
  .contact__cred { font-size: 21px; }
  .contact__role {
    color: var(--text-muted);
    font-size: 20px;
    margin-top: 2px;
  }
  .contact__address {
    font-size: 19px;
    line-height: 1.4;
    margin-top: 20px;
  }
  .contact__list { list-style: none; margin-top: 6px; }
  .contact__item {
    display: flex; align-items: center; gap: 10px;
    font-size: 19px; line-height: 1.45;
  }
  .contact__icon { width: 17px; height: 17px; flex: none; fill: var(--brand-blue); }

  .band-rule {
    position: absolute; left: 0; right: 0; top: 392px;
    height: 2px; background: #9da3a8;
  }
  .band {
    position: absolute; left: 0; right: 0; top: 398px; bottom: 0;
    background: var(--brand-blue);
  }

  /* Back */
  .back-brand {
    position: absolute;
    left: 0; right: 0; top: 118px;
    text-align: center;
  }
  .back-brand__dot {
    width: 110px; height: 110px; border-radius: 50%;
    background: var(--back-light);
    margin: 0 auto 20px;
  }
  .back-brand__name {
    color: var(--back-light);
    font-weight: 600;
    font-size: 32px;
    letter-spacing: 2px;
    text-transform: uppercase;
  }
  .back-brand__web {
    color: var(--back-light);
    font-style: italic;
    font-size: 21px;
    letter-spacing: 2.5px;
    margin-top: 12px;
  }
</style>
</head>
<body>

<section class="card card--front">
  <div class="brand">
    <div class="brand__dot"></div>
    <div class="brand__name">Carrington Hill Lodge</div>
  </div>

  <div class="divider"></div>

  <div class="contact">
    <div class="contact__name">Darren Pelham <span class="contact__cred">BCom</span></div>
    <div class="contact__role">Finance Manager</div>
    <div class="contact__address">48 Yarrabee Way<br>Birchwood, Qld 4215.</div>
    <ul class="contact__list">
      <li class="contact__item">
        <svg class="contact__icon" viewBox="0 0 24 24" aria-hidden="true"><path d="M6.6 10.8a15.1 15.1 0 0 0 6.6 6.6l2.2-2.2a1 1 0 0 1 1-.25 11.4 11.4 0 0 0 3.6.57 1 1 0 0 1 1 1V20a1 1 0 0 1-1 1A17 17 0 0 1 3 4a1 1 0 0 1 1-1h3.5a1 1 0 0 1 1 1c0 1.25.2 2.45.57 3.57a1 1 0 0 1-.25 1z"/></svg>
        0491 736 208
      </li>
      <li class="contact__item">
        <svg class="contact__icon" viewBox="0 0 24 24" aria-hidden="true"><path d="M2 5h20v14H2z M3 6l9 7 9-7" fill="none" stroke="#3f6c8c" stroke-width="2"/><path d="M2 5h20L12 12z"/></svg>
        dpelham@carringtonhilllodge.com.au
      </li>
      <li class="contact__item">
        <svg class="contact__icon" viewBox="0 0 24 24" aria-hidden="true"><circle cx="12" cy="12" r="10"/><path d="M2 12h20M12 2c3 3 3 17 0 20M12 2c-3 3-3 17 0 20" fill="none" stroke="#f1f1f3" stroke-width="1.5"/></svg>
        www.carringtonhilllodge.com.au
      </li>
    </ul>
  </div>

  <div class="band-rule"></div>
  <div class="band"></div>
</section>

<section class="card card--back">
  <div class="back-brand">
    <div class="back-brand__dot"></div>
    <div class="back-brand__name">Carrington Hill Lodge</div>
    <div class="back-brand__web">www.carringtonhilllodge.com.au</div>
  </div>
</section>

</body>
</html>
```